Whisker Nana offers loving cat sitting for your precious furbaby. The industry is cat care.

This will be a website which describes cat sitting services in Marin and Sonoma Counties. The site should include, (in no particular order...I'll leave that up to the designer:
Who I AM
My Services/Rates
A Place for Reviews
Cancellation Policy
My Qualifications
Availability (client will pick from the following times) Morning 8AM- Noon or Afternoon, Noon-6PM. Anytime 8Am to 6PM. 5% discount.
Service Area (Marin & Oakhill County CA). Use Google Map
Why Book Me?
A way to pay me (through Paypal including credit card option)
A Sit Reservation Request Form
Ask Questions/ Ask for a free consult
Contact Info - name, phone, email
Vacation Services
Sign up for newsletter
I have the logo, file below. Please use complimentary colors. I have many other photos to use which I cannot seem to upload here.

```html
<!DOCTYPE html>
<html lang="en">
<head>
<meta charset="utf-8">
<title>Whisker Nana — Loving Cat Sitting</title>
<link href="https://fonts.googleapis.com/css2?family=Libre+Baskerville:ital,wght@0,400;0,700;1,400&family=Montserrat:wght@400;500;600;700&display=swap" rel="stylesheet">
<style>
:root{
  --olive:#8d9a17;
  --olive-dark:#76830f;
  --plum:#5f3449;
  --plum-dark:#552c40;
  --ink:#2e2e2e;
  --muted:#7a7a7a;
  --white:#ffffff;
  --line:#cfd3a3;
}
*{box-sizing:border-box;margin:0;padding:0}
html,body{width:1200px;height:4979px;overflow:hidden}
body{font-family:"Montserrat",sans-serif;color:var(--ink);background:var(--white);position:relative}
section,header,footer{position:absolute;left:0;width:1200px}
.abs{position:absolute}
.btn{position:absolute;display:flex;align-items:center;justify-content:center;font-size:10px;font-weight:700;text-transform:uppercase;letter-spacing:.3px;background:var(--olive);color:var(--white);height:31px}
.btn.light{background:var(--white);color:var(--olive)}
.heading{font-family:"Libre Baskerville",serif;font-weight:700;text-transform:uppercase;color:var(--plum);font-size:28px;letter-spacing:.5px}
.copy{font-size:11px;line-height:19px;color:var(--muted)}
.photo{position:absolute}

/* header */
.site-header{top:0;height:112px;background:var(--white)}
.topbar{position:absolute;left:547px;top:0;width:653px;height:42px;background:var(--olive);clip-path:polygon(38px 0,100% 0,100% 100%,0 100%);color:var(--white);font-size:11px;display:flex;align-items:center;padding-left:50px;gap:16px}
.topbar svg{vertical-align:-2px;margin-right:5px}
.brand{position:absolute;left:196px;top:40px;display:flex;align-items:center;gap:10px}
.brand-mark{width:54px;height:54px;border-radius:50%;background:#e9ecc9}
.brand-name{font-family:"Libre Baskerville",serif;font-size:22px;color:var(--olive)}
.nav{position:absolute;left:440px;top:67px;display:flex;gap:18px;font-size:13px;font-weight:600;text-transform:uppercase;color:#333}
.nav .active{color:var(--olive)}
.phone-btn{position:absolute;left:873px;top:58px;width:134px;height:37px;background:var(--plum);color:var(--white);font-size:12px;display:flex;align-items:center;justify-content:center;gap:8px}

/* hero */
.hero{top:112px;height:500px}
.hero .photo{inset:0;background:linear-gradient(90deg,#3d3130 0%,#6f5a4f 35%,#a98e78 60%,#c9ad92 80%,#8c7a6a 100%)}
.hero-tag{position:absolute;left:193px;top:150px;font-family:"Libre Baskerville",serif;font-style:italic;font-size:16px;color:var(--white)}
.hero-title{position:absolute;left:193px;top:178px;font-family:"Libre Baskerville",serif;font-weight:700;font-size:56px;color:var(--white)}
.hero-copy{position:absolute;left:193px;top:255px;width:410px;font-size:12px;line-height:15px;color:var(--white)}

/* who */
.who{top:612px;height:439px}
.who-faint{left:0;top:230px;width:230px;height:209px;background:linear-gradient(180deg,#fbeeee,#f6dede);opacity:.7}
.portrait-ring{position:absolute;left:674px;top:49px;width:332px;height:332px;border-radius:50%;border:6px solid var(--olive);border-top-color:#f0f2dc;border-right-color:#f0f2dc;padding:8px}
.portrait-ring .photo{position:relative;width:100%;height:100%;border-radius:50%;background:linear-gradient(160deg,#8b8a86,#5d5a54 50%,#3e4547)}

/* services */
.services{top:1051px;height:885px;background:linear-gradient(90deg,#5b3346 0%,#6a3d51 55%,#7d5564 80%,#6b4656 100%)}
.services .heading{position:absolute;top:63px;width:100%;text-align:center;color:var(--white)}
.card{position:absolute;width:363px;height:194px;background:var(--white);text-align:center}
.card-bump{position:absolute;left:50%;top:-62px;width:136px;height:136px;margin-left:-68px;border-radius:50%;background:var(--white);border:3px solid var(--olive);border-bottom-color:transparent;border-right-color:transparent;transform:rotate(45deg)}
.card-icon{position:absolute;left:50%;top:-26px;width:54px;height:60px;margin-left:-27px;border:2px solid var(--olive);border-radius:12px;background:#f6f7e6}
.card h3{position:relative;margin-top:70px;font-family:"Libre Baskerville",serif;font-size:15px;letter-spacing:1px;font-weight:400;color:#222}
.card p{width:290px;margin:10px auto 0;font-size:10px;line-height:18px;color:var(--muted)}
.card-dot{position:absolute;left:50%;bottom:-16px;width:32px;height:32px;margin-left:-16px;border-radius:50%;background:var(--olive);border:4px solid #d8dca9}

/* qualifications */
.quals{top:1936px;height:417px}
.quals .photo{left:0;top:0;width:600px;height:417px;background:linear-gradient(135deg,#d7d2c4,#b8b09c 45%,#5f6a3a 85%,#3c4a22)}
.mascot{position:absolute;left:536px;top:2289px;width:128px;height:128px;border-radius:50%;background:var(--white);z-index:2;display:flex;align-items:center;justify-content:center}
.mascot span{width:84px;height:84px;border-radius:50%;background:#e9ecc9}

/* why */
.why{top:2353px;height:418px}
.why .photo{left:600px;top:0;width:600px;height:418px;background:linear-gradient(160deg,#c9c16a,#a6ab55 40%,#d8c9b4 70%,#8d8f3f)}

/* reviews */
.reviews{top:2771px;height:417px;background:linear-gradient(90deg,#7f8c14,#8e9b1f 50%,#7e8a15)}
.reviews .heading{position:absolute;top:46px;width:100%;text-align:center;color:var(--white)}
.avatar{position:absolute;left:554px;top:104px;width:92px;height:92px;border-radius:50%;border:3px solid var(--white);background:linear-gradient(160deg,#e6d2b5,#c9a987)}
.review-text{position:absolute;left:240px;top:217px;width:720px;text-align:center;color:var(--white);font-size:11px;line-height:19px}
.arrow{position:absolute;top:199px;width:18px;height:18px;border-radius:50%;background:var(--white);display:flex;align-items:center;justify-content:center}
.dots{position:absolute;top:290px;left:0;width:100%;display:flex;justify-content:center;gap:5px}
.dots i{width:8px;height:8px;border-radius:50%;background:var(--white);display:block}
.dots i.on{background:#4b4f20}

/* reservation */
.reserve{top:3188px;height:657px}
.field-label{position:absolute;font-size:10px;color:#333}
.field{position:absolute;height:45px;border:1px solid var(--olive);background:var(--white)}
.reason{position:absolute;left:164px;top:425px;width:477px;height:73px;border:1px solid var(--olive);padding:10px 10px;font-size:9px;color:#333;line-height:16px}
.reason div{display:flex;align-items:center;gap:6px}
.reason b{display:inline-block;width:9px;height:9px;border:1px solid #777}
.reason .caret{position:absolute;right:6px;bottom:6px;width:11px;height:11px;background:var(--olive)}
.contact-card{position:absolute;left:700px;top:71px;width:382px;height:518px;background:var(--white);box-shadow:0 0 18px rgba(0,0,0,.12);padding:58px 0 0 32px}
.contact-row{display:flex;gap:16px;margin-bottom:18px;font-size:13px;line-height:19px;color:#555;font-weight:500}
.contact-row svg{flex:none;margin-top:2px}

/* vacation */
.vacation{top:3845px;height:405px}
.vacation .photo{inset:0;background:linear-gradient(120deg,#eceae3 0%,#e6e4da 45%,#f2e6a8 70%,#d6e2ef 90%)}
.vac-panel{position:absolute;left:195px;top:0;width:369px;height:405px;background:var(--plum);color:var(--white);padding:34px 40px 0}
.vac-panel h4{font-family:"Libre Baskerville",serif;font-size:16px;font-weight:700;letter-spacing:.5px}
.vac-panel p{font-size:10px;line-height:13px;margin-top:12px;width:290px}
.vac-list{display:grid;grid-template-columns:125px 125px;row-gap:11px;margin-top:18px;font-size:10px}
.vac-list span::before{content:"";display:inline-block;width:7px;height:7px;border-radius:50%;background:var(--white);margin-right:12px;vertical-align:0}
.vac-rule{height:1px;background:rgba(255,255,255,.5);margin:28px 0 26px}

/* newsletter */
.newsletter{top:4250px;height:310px;text-align:center}
.newsletter .heading{position:absolute;top:55px;width:100%}
.newsletter .lead{position:absolute;top:108px;left:200px;width:800px;font-size:16px;line-height:23px;color:#666}
.news-input{position:absolute;top:207px;height:31px;border:1px solid #ddd;background:var(--white);font-size:9px;color:#444;display:flex;align-items:center;padding-left:22px}

/* footer */
.site-footer{top:4560px;height:419px}
.foot-wave{position:absolute;left:0;top:0}
.foot-col{position:absolute;top:98px;color:var(--white)}
.foot-col h5{font-family:"Libre Baskerville",serif;font-size:17px;font-weight:700;letter-spacing:.5px;text-transform:uppercase;margin-bottom:22px}
.foot-col ul{list-style:none}
.foot-col li{font-size:14px;margin-bottom:12px}
.foot-col li::before{content:"";display:inline-block;width:6px;height:6px;background:var(--white);margin-right:12px;vertical-align:3px}
.foot-contact li{display:flex;gap:14px;font-size:10px;line-height:16px;margin-bottom:10px}
.foot-contact li::before{display:none}
.foot-contact svg{flex:none}
.social li{font-size:10px;font-weight:700;text-transform:uppercase;display:flex;align-items:center;gap:10px;margin-bottom:15px}
.social li::before{display:none}
.social li i{display:inline-block;width:20px;height:20px;border:1.5px solid var(--white)}
.copyright{position:absolute;left:0;top:338px;width:1200px;height:81px;background:var(--plum-dark);color:var(--white);font-size:12px}
.copyright p{position:absolute;left:193px;top:33px}
.cards{position:absolute;left:719px;top:26px;display:flex;gap:12px}
.cards span{width:64px;height:30px;background:var(--white);color:var(--plum);font-size:10px;font-weight:700;display:flex;align-items:center;justify-content:center}
</style>
</head>
<body>

<header class="site-header">
  <div class="topbar">
    <span><svg width="11" height="11" viewBox="0 0 12 12"><circle cx="6" cy="6" r="5" fill="none" stroke="#fff" stroke-width="1.3"/><path d="M6 3v3l2 1.5" stroke="#fff" stroke-width="1.3" fill="none"/></svg>Availability : Mon-Sat: 8AM - 6PM</span>
    <span>|</span>
    <span><svg width="12" height="10" viewBox="0 0 12 10"><rect x=".7" y=".7" width="10.6" height="8.6" fill="none" stroke="#fff" stroke-width="1.2"/><path d="M1 1l5 4 5-4" stroke="#fff" stroke-width="1.2" fill="none"/></svg>Email : info@whiskernana.com</span>
  </div>
  <div class="brand"><span class="brand-mark"></span><span class="brand-name">Whisker Nana</span></div>
  <nav class="nav"><span class="active">Home</span><span>Who am I</span><span>Services</span><span>Reviews</span><span>Contact Us</span></nav>
  <div class="phone-btn"><svg width="12" height="12" viewBox="0 0 12 12"><path d="M2 1h3l1 3-2 1a7 7 0 0 0 3 3l1-2 3 1v3a1 1 0 0 1-1 1A10 10 0 0 1 1 2a1 1 0 0 1 1-1z" fill="#fff"/></svg>+1 555 014 2333</div>
</header>

<section class="hero">
  <div class="photo" role="img" aria-label="Woman smiling at a tabby cat in warm sunlight"></div>
  <p class="hero-tag">“ We Keep Your Cats &nbsp;Happy Anytime ”</p>
  <h1 class="hero-title">Whisker Nana</h1>
  <p class="hero-copy">Lorem Ipsum is simply dummy text of the printing and typesetting industry. Lorem Ipsum has been the industry's standard dummy text ever since the 1500s.</p>
  <span class="btn" style="left:193px;top:317px;width:147px">Make Appointment</span>
  <span class="btn light" style="left:367px;top:317px;width:108px">Call Now</span>
</section>

<section class="who">
  <div class="photo who-faint" role="img" aria-label="Faint illustration of a woman holding a cat"></div>
  <h2 class="heading abs" style="left:193px;top:70px">Who I Am?</h2>
  <p class="copy abs" style="left:193px;top:120px;width:435px">Lorem Ipsum is simply dummy text of the printing and typesetting industry. Ipsum has been the industry's standard dummy text ever since the 1500s, unknown printer took a galley of type and scrambled it to make a type book. It has survived not only five centuries, but also the leap into electronic typesetting, remaining essentially unchanged.</p>
  <p class="copy abs" style="left:193px;top:232px;width:435px">It was popularised in the 1960s with the release of Typeset Co sheets containing Ipsum passages, and more recently with desktop publishing software like PageForge including versions of Lorem Ipsum.</p>
  <span class="btn" style="left:193px;top:307px;width:109px">Read More</span>
  <div class="portrait-ring"><div class="photo" role="img" aria-label="Cat sitter kneeling beside two cats indoors"></div></div>
</section>

<section class="services">
  <h2 class="heading">My Services</h2>
  <div class="card" style="left:209px;top:212px"><span class="card-bump"></span><span class="card-icon" role="img" aria-label="Cat sitting icon"></span><h3>CAT &nbsp;SITTING</h3><p>It was popularised in the 1960s with the release of Typeset Co sheets containing Lorem Ipsum passages, and more recently with desktop publishing software like PageForge including versions of Lorem</p><span class="card-dot"></span></div>
  <div class="card" style="left:628px;top:212px"><span class="card-bump"></span><span class="card-icon" role="img" aria-label="Cat training icon"></span><h3>CAT &nbsp;TRAINING</h3><p>It was popularised in the 1960s with the release of Typeset Co sheets containing Lorem Ipsum passages, and more recently with desktop publishing software like PageForge including versions of Lorem</p><span class="card-dot"></span></div>
  <div class="card" style="left:209px;top:527px"><span class="card-bump"></span><span class="card-icon" role="img" aria-label="Cat walking icon"></span><h3>CAT &nbsp;WALKING</h3><p>It was popularised in the 1960s with the release of Typeset Co sheets containing Lorem Ipsum passages, and more recently with desktop publishing software like PageForge including versions of Lorem</p><span class="card-dot"></span></div>
  <div class="card" style="left:628px;top:527px"><span class="card-bump"></span><span class="card-icon" role="img" aria-label="Cat daycare icon"></span><h3>CAT &nbsp;DAYCARE</h3><p>It was popularised in the 1960s with the release of Typeset Co sheets containing Lorem Ipsum passages, and more recently with desktop publishing software like PageForge including versions of Lorem</p><span class="card-dot"></span></div>
  <span class="btn" style="left:545px;top:781px;width:110px">View More</span>
</section>

<section class="quals">
  <div class="photo" role="img" aria-label="Woman feeding a black cat among green plants"></div>
  <h2 class="heading abs" style="left:657px;top:70px">My Qualifications</h2>
  <p class="copy abs" style="left:657px;top:118px;width:365px">Lorem Ipsum is simply dummy text of the printing and typeset Ipsum has been the industry's standard dummy text ever since unknown printer took a galley of type and scrambled it to make book. It has survived not only five centuries, but also the leap typesetting, remaining essentially unchanged.</p>
  <p class="copy abs" style="left:657px;top:232px;width:365px">It was popularised in the 1960s with the release of Typeset Co Ipsum passages, and more recently with desktop publishing PageForge including versions of Lorem Ipsum.</p>
  <span class="btn" style="left:657px;top:309px;width:116px">Read More</span>
</section>

<section class="why">
  <h2 class="heading abs" style="left:193px;top:70px">Why Book Me?</h2>
  <p class="copy abs" style="left:193px;top:116px;width:375px">Lorem Ipsum is simply dummy text of the printing and typeset Ipsum has been the industry's standard dummy text ever since unknown printer took a galley of type and scrambled it to make book. It has survived not only five centuries, but also the leap typesetting, remaining essentially unchanged.</p>
  <p class="copy abs" style="left:193px;top:230px;width:375px">It was popularised in the 1960s with the release of Typeset Co Ipsum passages, and more recently with desktop publishing PageForge including versions of Lorem Ipsum.</p>
  <span class="btn" style="left:193px;top:309px;width:118px">Book Now</span>
  <div class="photo" role="img" aria-label="Woman feeding a white kitten with a bottle outdoors"></div>
</section>
<div class="mascot"><span></span></div>

<section class="reviews">
  <h2 class="heading">Client Reviews</h2>
  <div class="avatar" role="img" aria-label="Client portrait"></div>
  <span class="arrow" style="left:175px"><svg width="8" height="8" viewBox="0 0 8 8"><path d="M5.5 1L2.5 4l3 3" stroke="#7e8a15" stroke-width="1.6" fill="none"/></svg></span>
  <span class="arrow" style="left:999px"><svg width="8" height="8" viewBox="0 0 8 8"><path d="M2.5 1l3 3-3 3" stroke="#7e8a15" stroke-width="1.6" fill="none"/></svg></span>
  <p class="review-text">Lorem Ipsum is simply dummy text of the printing and typeset Ipsum has been the industry's standard dummy text ever since unknown printer took a galley of type and scrambled it to make book. It has survived not only five centuries, but also the leap typesetting, remaining essentially unchanged.</p>
  <div class="dots"><i></i><i></i><i class="on"></i><i></i></div>
  <span class="btn light" style="left:545px;top:332px;width:110px;color:var(--plum)">View More</span>
</section>

<section class="reserve">
  <h2 class="heading abs" style="left:164px;top:85px">Sit Reservation Request</h2>
  <p class="copy abs" style="left:164px;top:136px;width:470px;font-size:10px">Contrary to popular belief, Lorem Ipsum is not simply random text. It has roots in a piece of classical Latin literature from 45 BC, making it over 2000 years old. Robert Calloway, a Latin professor at Hollins Ridge College in Virginia, looked up one</p>
  <span class="field-label" style="left:164px;top:226px">First Name</span>
  <span class="field-label" style="left:415px;top:226px">Last Name</span>
  <span class="field" style="left:164px;top:251px;width:228px"></span>
  <span class="field" style="left:415px;top:251px;width:226px"></span>
  <span class="field-label" style="left:164px;top:312px">Contact Number</span>
  <span class="field-label" style="left:415px;top:312px">Select A Date</span>
  <span class="field" style="left:164px;top:338px;width:228px"></span>
  <span class="field" style="left:415px;top:338px;width:226px"></span>
  <span class="field-label" style="left:164px;top:400px">Reason For A Reservation</span>
  <div class="reason"><div><b></b>Cat Sitting</div><div><b></b>Cat Training</div><div><b></b>Cat Walking</div><span class="caret"></span></div>
  <span class="btn" style="left:164px;top:535px;width:120px">Book Now</span>

  <div class="contact-card">
    <div class="contact-row"><svg width="22" height="26" viewBox="0 0 22 26"><path d="M11 1a8 8 0 0 1 8 8c0 6-8 15-8 15S3 15 3 9a8 8 0 0 1 8-8z" fill="none" stroke="#8d9a17" stroke-width="1.6"/><circle cx="11" cy="9" r="3" fill="none" stroke="#8d9a17" stroke-width="1.6"/></svg><span>It is a long established fact that a<br>reader will be<br>00417</span></div>
    <div class="contact-row"><svg width="22" height="22" viewBox="0 0 22 22"><path d="M4 2h5l2 5-3 2a11 11 0 0 0 5 5l2-3 5 2v5a2 2 0 0 1-2 2A18 18 0 0 1 2 4a2 2 0 0 1 2-2z" fill="none" stroke="#8d9a17" stroke-width="1.6"/></svg><span>Set Reservation:<br>+1 555 0176 876</span></div>
    <div class="contact-row"><svg width="22" height="22" viewBox="0 0 22 22"><path d="M4 2h5l2 5-3 2a11 11 0 0 0 5 5l2-3 5 2v5a2 2 0 0 1-2 2A18 18 0 0 1 2 4a2 2 0 0 1 2-2z" fill="none" stroke="#8d9a17" stroke-width="1.6"/></svg><span>Cancellation Policy :<br>+1 555 0176 876</span></div>
    <div class="contact-row"><svg width="22" height="18" viewBox="0 0 22 18"><rect x="1" y="2" width="20" height="14" fill="none" stroke="#8d9a17" stroke-width="1.6"/><path d="M1 2l10 8 10-8" fill="none" stroke="#8d9a17" stroke-width="1.6"/></svg><span>Email Us :<br>hello@whiskernana.com</span></div>
    <div class="contact-row"><svg width="22" height="22" viewBox="0 0 22 22"><rect x="2" y="8" width="18" height="10" fill="none" stroke="#8d9a17" stroke-width="1.6"/><rect x="6" y="2" width="10" height="6" fill="none" stroke="#8d9a17" stroke-width="1.6"/><rect x="6" y="14" width="10" height="6" fill="#fff" stroke="#8d9a17" stroke-width="1.6"/></svg><span>Fax Us :<br>+1 555 0176 876</span></div>
    <div class="contact-row"><svg width="22" height="22" viewBox="0 0 22 22"><circle cx="11" cy="11" r="9" fill="none" stroke="#8d9a17" stroke-width="1.6"/><path d="M11 5v6l4 3" fill="none" stroke="#8d9a17" stroke-width="1.6"/></svg><span>Working Hours:<br>Monday - Friday : 8.00 AM - 1.00 PM<br>Saturday : 1.00 PM - 6.00 PM<br>Anytime &nbsp;: 8.00 AM - 6.00 PM</span></div>
  </div>
</section>

<section class="vacation">
  <div class="photo" role="img" aria-label="Street map of the service area"></div>
  <div class="vac-panel">
    <h4>VACATION SERVICES</h4>
    <p>It is a long established fact that a reader will be distracted by the readable content of a page when looking at its layout.</p>
    <div class="vac-list"><span>Lorem Ipsum</span><span>Lorem Ipsum</span><span>Lorem Ipsum</span><span>Lorem Ipsum</span><span>Lorem Ipsum</span><span>Lorem Ipsum</span><span>Lorem Ipsum</span><span>Lorem Ipsum</span><span>Lorem Ipsum</span><span>Lorem Ipsum</span></div>
    <div class="vac-rule"></div>
    <h4>SERVICE AREAS</h4>
    <p>It is a long established fact that a reader will be distracted by the readable content of a</p>
    <div class="vac-list"><span>Bayview , CA</span><span>Oakhill County CA</span></div>
  </div>
</section>

<section class="newsletter">
  <h2 class="heading">Sign Up For Newsletter</h2>
  <p class="lead">It is a long established fact that a reader will be distracted by the readable content of a page when looking at its layout. The point of using Lorem Ipsum</p>
  <span class="news-input" style="left:332px;width:192px">Name</span>
  <span class="news-input" style="left:543px;width:193px">Email Address*</span>
  <span class="btn" style="left:757px;top:207px;width:114px">Sign Up</span>
</section>

<footer class="site-footer">
  <svg class="foot-wave" width="1200" height="338" viewBox="0 0 1200 338"><path d="M0 50 C220 10 420 0 620 30 S980 60 1200 0 V338 H0 Z" fill="#8d9a17"/></svg>
  <div class="foot-col" style="left:199px"><h5>Quick Links</h5><ul><li>Home</li><li>Why I Am</li><li>Our Services</li><li>Our Reviews</li><li>Contact Us</li></ul></div>
  <div class="foot-col" style="left:383px"><h5>Other Links</h5><ul><li>Cancellation Policy</li><li>Sit Reservation</li><li>Free consultation</li><li>Vacation Services</li><li>Make A Payment</li></ul></div>
  <div class="foot-col foot-contact" style="left:605px"><h5>Contact Now</h5><ul>
    <li><svg width="20" height="22" viewBox="0 0 20 22"><path d="M10 1a7 7 0 0 1 7 7c0 5-7 13-7 13S3 13 3 8a7 7 0 0 1 7-7z" fill="#fff"/></svg><span>Contrary to popular belief,<br>Lorem Ipsum is not simply text.</span></li>
    <li><svg width="20" height="20" viewBox="0 0 20 20"><rect x="3" y="2" width="14" height="16" fill="#fff"/></svg><span style="padding-top:2px">555-345-6789</span></li>
    <li><svg width="20" height="20" viewBox="0 0 22 22"><path d="M4 2h5l2 5-3 2a11 11 0 0 0 5 5l2-3 5 2v5a2 2 0 0 1-2 2A18 18 0 0 1 2 4a2 2 0 0 1 2-2z" fill="#fff"/></svg><span style="padding-top:2px">555-345-6789</span></li>
    <li><svg width="22" height="16" viewBox="0 0 22 16"><rect x="0" y="0" width="22" height="16" fill="#fff"/><path d="M1 1l10 8 10-8" fill="none" stroke="#8d9a17" stroke-width="1.6"/></svg><span>info@whiskernana.com</span></li>
  </ul></div>
  <div class="foot-col social" style="left:883px"><h5>Follow Us</h5><ul><li><i></i>Friendbook</li><li><i></i>Circle Plus</li><li><i></i>WorkLink</li><li><i></i>Snapgram</li></ul></div>
  <div class="copyright">
    <p>Copyright © 2021 Whisker Nana.All Rights Reserved.</p>
    <div class="cards"><span>PayCard</span><span>CardOne</span><span>AmPay</span><span>NovaPay</span></div>
  </div>
</footer>

</body>
</html>
```